Ward Compass Business Card Design*

We need a business card design for our company Ward Compass. Our company is specialized in providing online consulting services regarding medical institutions, hospitals and doctors. We work with patients worldwide looking to choose between healthcare providers. We have a website you may use as a reference, where we list doctors and clinics worldwide. So we target Medical providers as well as patients worldwide.
Target Market(s)
Medical Providers and patients around the world
Industry/Entity Type
Medical
Contact Information for Business Card
Salma Derkaoui
CEO
+90 612 348 2071
info@wardcompass-example.com
www.wardcompass-example.com
14 Annakhil 3 H.R.B. Rabat, Morocco
Requirements
Must have
- Company logo/name on one full side, personal info and smaller logo and company name on the other side.
Nice to have
- Smart and elegant design

```html
<!DOCTYPE html>
<html lang="en">
<head>
<meta charset="utf-8">
<title>Ward Compass – Business Card</title>
<link rel="stylesheet" href="https://fonts.googleapis.com/css2?family=Montserrat:wght@400;600;700&family=Poppins:wght@400&display=swap">
<style>
  :root {
    --navy: #1b3a66;
    --grey: #7d7d7f;
    --ink: #3a3a3c;
    --paper: #ffffff;
    --backdrop: #2a2b2e;
  }
  * { margin: 0; padding: 0; box-sizing: border-box; }
  html, body { width: 1200px; height: 800px; overflow: hidden; }
  body {
    background: var(--backdrop);
    position: relative;
    font-family: "Poppins", sans-serif;
  }
  .card {
    position: absolute;
    left: 300px;
    width: 600px;
    height: 343px;
    overflow: hidden;
  }
  .card--back { top: 40px; background: var(--navy); }
  .card--front { top: 413px; background: var(--paper); }

  .brand {
    position: absolute;
    display: flex;
    align-items: center;
    gap: 14px;
    left: 50%;
    transform: translateX(-50%);
    white-space: nowrap;
  }
  .brand__dot {
    border-radius: 50%;
    flex: none;
  }
  .brand__name {
    font-family: "Montserrat", sans-serif;
    font-weight: 600;
    text-transform: uppercase;
    letter-spacing: 1px;
  }

  /* back side */
  .card--back .brand { top: 110px; }
  .card--back .brand__dot { width: 58px; height: 58px; background: var(--paper); }
  .card--back .brand__name { font-size: 36px; color: var(--paper); }
  .back-web {
    position: absolute;
    top: 208px;
    width: 100%;
    text-align: center;
    color: var(--paper);
    font-size: 15px;
    letter-spacing: 1px;
  }

  /* front side */
  .card--front .brand { top: 48px; }
  .card--front .brand__dot { width: 44px; height: 44px; background: var(--navy); }
  .card--front .brand__name { font-size: 28px; color: var(--navy); }

  .person {
    position: absolute;
    left: 60px;
    top: 142px;
    width: 215px;
    text-align: right;
  }
  .person__name {
    font-family: "Montserrat", sans-serif;
    font-weight: 700;
    font-size: 20px;
    color: var(--navy);
    letter-spacing: 0.5px;
    white-space: nowrap;
  }
  .person__role {
    font-size: 14px;
    color: var(--ink);
    margin-top: 2px;
  }
  .divider {
    position: absolute;
    left: 292px;
    top: 168px;
    width: 1.5px;
    height: 48px;
    background: var(--navy);
  }
  .contacts {
    position: absolute;
    left: 306px;
    top: 164px;
    list-style: none;
    font-size: 13px;
    color: var(--ink);
    line-height: 19px;
  }
  .contacts li { display: flex; align-items: center; gap: 7px; white-space: nowrap; }
  .contacts svg { width: 12px; height: 12px; flex: none; fill: var(--navy); }
  .address {
    position: absolute;
    left: 88px;
    top: 232px;
    font-size: 14px;
    color: var(--ink);
    white-space: nowrap;
  }
  .edge-bands {
    position: absolute;
    left: 0;
    bottom: 0;
    width: 600px;
    height: 70px;
  }
</style>
</head>
<body>

  <section class="card card--back" aria-label="Business card, back side">
    <div class="brand">
      <span class="brand__dot"></span>
      <span class="brand__name">Ward Compass</span>
    </div>
    <p class="back-web">www.wardcompass-example.com</p>
  </section>

  <section class="card card--front" aria-label="Business card, front side">
    <div class="brand">
      <span class="brand__dot"></span>
      <span class="brand__name">Ward Compass</span>
    </div>

    <div class="person">
      <p class="person__name">SALMA DERKAOUI</p>
      <p class="person__role">CEO</p>
    </div>

    <span class="divider"></span>

    <ul class="contacts">
      <li>
        <svg viewBox="0 0 24 24" aria-hidden="true"><path d="M6.6 10.8a15 15 0 0 0 6.6 6.6l2.2-2.2a1 1 0 0 1 1-.25 11.4 11.4 0 0 0 3.6.57 1 1 0 0 1 1 1V20a1 1 0 0 1-1 1A17 17 0 0 1 3 4a1 1 0 0 1 1-1h3.5a1 1 0 0 1 1 1c0 1.25.2 2.45.57 3.57a1 1 0 0 1-.25 1z"/></svg>
        +90 612 348 2071
      </li>
      <li>
        <svg viewBox="0 0 24 24" aria-hidden="true"><path d="M2 5h20v14H2z M2 5l10 8 10-8" /></svg>
        info@wardcompass-example.com
      </li>
      <li>
        <svg viewBox="0 0 24 24" aria-hidden="true"><circle cx="12" cy="12" r="10" fill="none" stroke="#1b3a66" stroke-width="2"/><path d="M2 12h20M12 2c3 3 3 17 0 20M12 2c-3 3-3 17 0 20" fill="none" stroke="#1b3a66" stroke-width="1.6"/></svg>
        www.wardcompass-example.com
      </li>
    </ul>

    <p class="address">14 Annakhil 3 H.R.B. Rabat, Morocco</p>

    <svg class="edge-bands" viewBox="0 0 600 70" aria-hidden="true">
      <polygon points="0,22 262,60 248,70 0,70" fill="var(--navy)"/>
      <polygon points="262,60 600,60 600,70 248,70" fill="var(--grey)"/>
    </svg>
  </section>

</body>
</html>
```